Webdesign für Getränkelogistik & Full-Service-Partner bei Events
Zielgruppe
Getränkelogistiker und Full-Service-Partner bei Events
Zielgruppe: Getränke-EinzelHändler; Veranstalter von Events und privaten Feiern
Aufgabenstellung
- soll „Frische“ und „Moderne“ vermitteln, ohne eine Getränkeart in den Vordergrund zu rücken
- soll von den Farben her gut zum Logo passen (siehe Anlagen)
- Slider wäre wünschenswert
- Slogan 'Wir freuen uns auf Sie!'

```html
<!DOCTYPE html>
<html lang="de">
<head>
<meta charset="utf-8">
<title>Getränke Hollmann GmbH</title>
<link rel="stylesheet" href="https://fonts.googleapis.com/css2?family=Open+Sans:ital,wght@0,400;0,600;0,700;1,400&family=Playfair+Display:wght@400;700&display=swap">
<style>
:root{
  --green:#1b5e4a;
  --yellow:#f6bd00;
  --text:#3a3a3a;
  --muted:#8a8a8a;
  --line:#cfcfcf;
  --panel:#f3f3f3;
  --white:#ffffff;
}
*{box-sizing:border-box;margin:0;padding:0}
html,body{width:979px;height:1200px;overflow:hidden;background:var(--white)}
body{font-family:"Open Sans",sans-serif;color:var(--text);position:relative}
.abs{position:absolute}
.brand{left:0;width:979px;top:24px;display:flex;justify-content:center;align-items:center;gap:8px}
.brand-dot{width:22px;height:22px;border-radius:50%;background:var(--yellow)}
.brand-name{font-family:"Playfair Display",serif;font-weight:700;font-size:22px;color:var(--green)}
.nav{left:190px;width:600px;top:77px;height:40px;border-top:1px solid var(--line);border-bottom:1px solid var(--line);display:flex;justify-content:center;align-items:center;gap:24px;font-size:9.6px}
.nav a{color:var(--text);text-decoration:none}
.nav a.active{color:var(--green);font-weight:700}
.hero{left:120px;top:132px;width:738px;height:360px;overflow:hidden;background:radial-gradient(ellipse 55% 70% at 66% 45%,#34b034 0%,#1c8a1e 40%,#0e5a10 75%,#063006 100%)}
.hero-photo{position:absolute;inset:0;background:
  radial-gradient(ellipse 12% 42% at 58% 58%,rgba(4,60,12,.55),rgba(4,60,12,0) 100%),
  radial-gradient(ellipse 11% 40% at 90% 60%,rgba(4,60,12,.5),rgba(4,60,12,0) 100%),
  radial-gradient(ellipse 48% 20% at 74% 104%,rgba(232,244,232,.85) 0%,rgba(200,230,200,.45) 50%,rgba(200,230,200,0) 100%),
  linear-gradient(90deg,rgba(3,30,3,.35) 0%,rgba(3,30,3,0) 35%)}
.slogan{position:absolute;left:70px;top:102px;font-family:"Playfair Display",serif;font-size:34px;line-height:38px;color:var(--yellow)}
.thumbs{position:absolute;left:70px;top:309px;display:flex;gap:5px}
.thumb{width:36px;height:36px}
.thumb.active{border:2px solid var(--yellow)}
.hotline{left:849px;top:147px;width:130px;height:49px;background:var(--yellow);padding:7px 0 0 10px}
.hotline-label{font-size:10.5px;color:var(--green)}
.hotline-number{font-size:17.5px;font-weight:700;color:var(--green);line-height:21px;white-space:nowrap}
.service{top:551px;width:140px}
.service-label{font-size:9px;font-weight:600;color:var(--yellow);height:21px}
.service-rule{width:26px;height:1px;background:var(--line)}
.service-title{font-family:"Playfair Display",serif;font-weight:700;font-size:19.5px;color:var(--green);margin-top:14px;margin-left:-1px;white-space:nowrap}
.service-text{font-size:9.5px;line-height:14.3px;margin-top:18px;height:72px}
.service-img{width:139px;height:94px;margin-top:9px}
.service-more{display:block;text-align:right;margin-top:14px;font-size:10px;font-weight:600;color:var(--green);text-decoration:underline}
.contact{left:120px;top:871px;width:738px;height:278px;background:var(--panel)}
.contact-title{position:absolute;left:70px;top:15px;width:600px;font-family:"Playfair Display",serif;font-weight:700;font-size:20px;color:var(--green);border-bottom:1px solid var(--line);padding-bottom:2px}
.field{position:absolute;height:20px;width:139px;background:var(--white);font-size:9px;font-style:italic;color:var(--muted);padding:4px 8px}
.field.message{width:292px;height:105px}
.btn{position:absolute;width:87px;height:20px;background:var(--green);color:var(--yellow);font-size:8px;font-weight:700;text-align:center;line-height:20px}
.info{position:absolute;font-size:9.5px;line-height:14.3px}
.info-row{display:flex;gap:4px}
.info svg{flex:none;margin-top:3px}
.map{position:absolute;left:376px;top:120px;width:294px;height:105px;background:linear-gradient(135deg,#dfeedd,#eef3e8 50%,#d6e9d3)}
.footer{left:0;width:979px;top:1164px;text-align:center;font-size:9.5px}
</style>
</head>
<body>
<div class="abs brand"><span class="brand-dot"></span><span class="brand-name">Getränke Hollmann</span></div>

<nav class="abs nav">
  <a class="active" href="#">Home</a><a href="#">Unternehmen</a><a href="#">Team</a><a href="#">Großhandel</a><a href="#">Rund um Ihr Event</a><a href="#">Karriere</a><a href="#">Kontakt</a>
</nav>

<section class="abs hero">
  <div class="hero-photo" role="img" aria-label="Zwei grüne Flaschen auf Eiswürfeln vor grünem Hintergrund"></div>
  <p class="slogan">“Wir freuen uns<br>auf Sie!”</p>
  <div class="thumbs">
    <div class="thumb active" style="background:#1b6b1b" role="img" aria-label="Vorschau Flaschen"></div>
    <div class="thumb" style="background:#c8583a" role="img" aria-label="Vorschau Anstoßen"></div>
    <div class="thumb" style="background:#b04a18" role="img" aria-label="Vorschau Weingläser"></div>
    <div class="thumb" style="background:#6fbad0" role="img" aria-label="Vorschau Erfrischungsgetränk"></div>
  </div>
</section>

<div class="abs hotline"><div class="hotline-label">Bestell-Hotline:</div><div class="hotline-number">01234 567890</div></div>

<article class="abs service" style="left:190px">
  <div class="service-label">SERVICE 01</div><div class="service-rule"></div>
  <h2 class="service-title">Für Ihr Event</h2>
  <p class="service-text">Dies ist ein Typoblindtext. An ihm kann man sehen, ob alle Buchstaben da sind und wie sie aussehen.</p>
  <div class="service-img" style="background:linear-gradient(160deg,#4b5a8a,#c9ccd6 55%,#e8e8ea)" role="img" aria-label="Festlich dekorierter Eventbereich mit Zelt"></div>
  <a class="service-more" href="#">weiterlesen</a>
</article>
<article class="abs service" style="left:343px">
  <div class="service-label">SERVICE 02</div><div class="service-rule"></div>
  <h2 class="service-title">Großhandel</h2>
  <p class="service-text">Dies ist ein Typoblindtext. An ihm kann man sehen, ob alle Buchstaben da sind und wie sie aussehen.</p>
  <div class="service-img" style="background:linear-gradient(180deg,#d6d9d8 0%,#d6d9d8 25%,#1f5a34 45%,#1f5a34 80%,#5d5f60 100%)" role="img" aria-label="Grüne Lieferwagen vor dem Lager"></div>
  <a class="service-more" href="#">weiterlesen</a>
</article>
<article class="abs service" style="left:496px">
  <div class="service-label">SERVICE 03</div><div class="service-rule"></div>
  <h2 class="service-title">Unternehmen</h2>
  <p class="service-text">Dies ist ein Typoblindtext. An ihm kann man sehen, ob alle Buchstaben da sind und wie sie aussehen.</p>
  <div class="service-img" style="background:linear-gradient(135deg,#b8bdbd,#e9ebeb 50%,#9da3a6)" role="img" aria-label="Geschäftsführer am Treppengeländer"></div>
  <a class="service-more" href="#">weiterlesen</a>
</article>
<article class="abs service" style="left:650px">
  <div class="service-label">SERVICE 04</div><div class="service-rule"></div>
  <h2 class="service-title">Team</h2>
  <p class="service-text">Dies ist ein Typoblindtext. An ihm kann man sehen, ob alle Buchstaben da sind und wie sie aussehen.</p>
  <div class="service-img" style="background:linear-gradient(180deg,#3a3b36,#6b6d62 50%,#2f4a36)" role="img" aria-label="Mitarbeiterteam in der Lagerhalle"></div>
  <a class="service-more" href="#">weiterlesen</a>
</article>

<section class="abs contact">
  <h2 class="contact-title">Kontaktieren Sie uns</h2>
  <div class="field" style="left:70px;top:64px">Ihr Vorname</div>
  <div class="field" style="left:223px;top:64px">Ihr Nachname</div>
  <div class="field" style="left:70px;top:93px">Ihre Telefonnummer</div>
  <div class="field" style="left:223px;top:93px">Ihre E-Mail-Adresse</div>
  <div class="field message" style="left:70px;top:120px">Ihre Nachricht...</div>
  <div class="btn" style="left:70px;top:232px">ABSENDEN</div>

  <div class="info" style="left:376px;top:60px">
    <div class="info-row"><svg width="7" height="9" viewBox="0 0 7 9"><path d="M3.5 0A3.5 3.5 0 0 0 0 3.5C0 6 3.5 9 3.5 9S7 6 7 3.5A3.5 3.5 0 0 0 3.5 0Zm0 5a1.4 1.4 0 1 1 0-2.8 1.4 1.4 0 0 1 0 2.8Z" fill="var(--green)"/></svg><span>Getränke Hollmann GmbH<br>Am Lindenhof 4<br>01234 Talheim</span></div>
  </div>
  <div class="info" style="left:517px;top:60px">
    <div class="info-row"><svg width="9" height="9" viewBox="0 0 9 9"><path d="M2 0l1.6 2.2-1 1.1a6 6 0 0 0 3.1 3.1l1.1-1L9 7l-1 2C4 9 0 5 0 1Z" fill="var(--green)"/></svg><span>Tel.: +49 1234 567890<br>Fax: +49 1234 567891</span></div>
    <div class="info-row"><svg width="9" height="7" viewBox="0 0 9 7"><rect width="9" height="7" rx="1" fill="var(--green)"/><path d="M0 1l4.5 3L9 1" stroke="#fff" fill="none" stroke-width=".8"/></svg><span>info(at)getraenke-hollmann.de</span></div>
  </div>
  <div class="map" role="img" aria-label="Straßenkarte mit Firmenstandort"></div>
  <div class="btn" style="left:377px;top:232px">KARTE ÖFFNEN</div>
</section>

<footer class="abs footer">Downloads &nbsp;|&nbsp; Kontakt &nbsp;|&nbsp; Impressum / Datenschutz &nbsp;|&nbsp; AGB &nbsp;|&nbsp; © 2020 getraenke-hollmann.de</footer>
</body>
</html>
```